BRD business cards Dr. Martin Velk

I need a business card designed for our dental office. We are a "general dental" practice.
Looking for a clean, professional but not too fancy design with our logo and contact information required.
front of card is information/standard business card, backside is appt reminder with lines for date and time of appt
doctors name: Dr. Martin Velk DMD
office name: Velk Family Dental
address: 4827 E Tolland Ave Coral Springs, FL 33065
phone: 954-555-0173
Dentistry
Office name, Doctor name, address, phone number...etc
- White/off white base color, blue and or black lettering

```html
<!DOCTYPE html>
<html lang="en">
<head>
<meta charset="utf-8">
<title>Velk Family Dental – Business Card</title>
<link rel="stylesheet" href="https://fonts.googleapis.com/css2?family=Tinos:wght@400;700&family=Arimo:wght@400&display=swap">
<style>
  :root {
    --backdrop: #3f6f6e;
    --card: #fdfdf8;
    --brand-blue: #0d4ea6;
    --ink-gray: #555555;
    --rule: #3a3a3a;
    --dots: #666666;
  }
  * { box-sizing: border-box; margin: 0; padding: 0; }
  html, body { width: 1200px; height: 715px; overflow: hidden; }
  body {
    background: var(--backdrop);
    position: relative;
    font-family: "Tinos", "Times New Roman", serif;
  }
  .card {
    position: absolute;
    top: 214px;
    width: 500px;
    height: 286px;
    background: var(--card);
    border-radius: 18px;
    box-shadow: 0 10px 28px rgba(0,0,0,0.28);
  }
  .card--front { left: 60px; }
  .card--back { left: 640px; }

  /* front */
  .brand {
    position: absolute;
    left: 28px; top: 0;
    width: 200px; height: 286px;
    display: flex; flex-direction: column;
    align-items: center; justify-content: center;
    gap: 14px;
  }
  .brand__dot {
    width: 54px; height: 54px;
    border-radius: 50%;
    background: var(--brand-blue);
  }
  .brand__name {
    color: var(--brand-blue);
    font-size: 21px;
    font-weight: 400;
    letter-spacing: 1px;
    text-transform: uppercase;
    text-align: center;
    line-height: 1.15;
  }
  .divider {
    position: absolute;
    left: 250px; top: 48px;
    width: 1px; height: 190px;
    background: var(--rule);
  }
  .doctor {
    position: absolute;
    left: 262px; right: 16px; top: 70px;
    text-align: center;
    color: var(--ink-gray);
  }
  .doctor__name { font-size: 27px; font-weight: 700; }
  .doctor__title { font-size: 17px; margin-top: 2px; }
  .contact {
    position: absolute;
    left: 278px; top: 160px;
    color: var(--brand-blue);
    font-size: 16px;
    line-height: 1.3;
  }
  .contact__row { display: flex; align-items: flex-start; gap: 9px; margin-bottom: 8px; }
  .contact__icon { width: 20px; height: 20px; flex: none; margin-top: 1px; }

  /* back */
  .reminder {
    position: absolute;
    left: 34px; right: 34px; top: 124px;
    display: flex; align-items: baseline;
    font-family: "Arimo", Arial, sans-serif;
    font-size: 15px;
    color: var(--ink-gray);
  }
  .reminder__field { display: flex; align-items: baseline; flex: 1; }
  .reminder__field + .reminder__field { margin-left: 10px; }
  .reminder__line {
    flex: 1;
    margin-left: 4px;
    border-bottom: 2px dotted var(--dots);
    height: 1px;
  }
</style>
</head>
<body>
  <section class="card card--front" aria-label="Business card front">
    <div class="brand">
      <div class="brand__dot"></div>
      <div class="brand__name">Velk Family Dental</div>
    </div>
    <div class="divider"></div>
    <div class="doctor">
      <div class="doctor__name">Dr. Martin Velk</div>
      <div class="doctor__title">DMD</div>
    </div>
    <div class="contact">
      <div class="contact__row">
        <svg class="contact__icon" viewBox="0 0 20 20" aria-hidden="true">
          <circle cx="10" cy="10" r="10" fill="#0d4ea6"/>
          <path d="M7.2 5.2c.6-.3 1.1 0 1.3.6l.5 1.5c.1.4 0 .8-.4 1l-.7.5c.5 1.2 1.3 2.1 2.4 2.7l.6-.6c.3-.3.7-.4 1.1-.2l1.4.7c.5.3.7.8.4 1.3-.7 1.3-2 1.7-3.4 1-2.5-1.2-4.1-3.3-4.5-5.9-.2-1.2.4-2.2 1.3-2.6z" fill="#fdfdf8"/>
        </svg>
        <span>954-555-0173</span>
      </div>
      <div class="contact__row">
        <svg class="contact__icon" viewBox="0 0 20 20" aria-hidden="true">
          <circle cx="10" cy="10" r="10" fill="#0d4ea6"/>
          <path d="M10 4.5 4.5 9.5h1.6v5h3v-3h1.8v3h3v-5h1.6z" fill="#fdfdf8"/>
        </svg>
        <span>4827 E Tolland Ave<br>Palm Crest, FL 33090</span>
      </div>
    </div>
  </section>

  <section class="card card--back" aria-label="Appointment reminder back">
    <div class="reminder">
      <div class="reminder__field"><span>Date</span><span class="reminder__line"></span></div>
      <div class="reminder__field"><span>Time</span><span class="reminder__line"></span></div>
    </div>
  </section>
</body>
</html>
```